Plumwick Home - High Quality Organic Cleaning Product

A product label for a foaming hand soap. Company is called "Plumwick Home" and the tagline is "The Plumwick Promise". Maybe lighter blue background with red letters, but open to what looks good. Want it to be a simple, clean and sophisticated design that looks fresh and stands out. This product has high quality organic ingredients hence the ingredients are "plumwick home" than other toxic chemical cleaners. Attached is label specifications as well as an image for stock language for left and right side of label for reference. Parts can be omitted, added or mixed and matched as needed.
Went on vacation/holiday
Moms

```html
<!DOCTYPE html>
<html lang="en">
<head>
<meta charset="utf-8">
<title>Plumwick Home – Foaming Hand Soap Label</title>
<link rel="stylesheet" href="https://fonts.googleapis.com/css2?family=DM+Serif+Text&family=Montserrat:wght@500;600;700&display=swap">
<style>
  :root {
    --backdrop: #fdb4b3;
    --label-white: #ffffff;
    --band-pink: #e9939b;
    --band-pink-deep: #dc7f89;
    --tag-red: #c9485a;
    --soap-blue: #2f7cc0;
    --icon-blue: #3b7fb8;
    --ink-dark: #2e2e38;
    --stripe-pink: #e3a3a9;
  }
  * { box-sizing: border-box; margin: 0; padding: 0; }
  html, body {
    width: 1200px; height: 1200px; overflow: hidden;
    background: var(--backdrop);
  }
  .canvas {
    position: relative; width: 1200px; height: 1200px;
    display: flex; align-items: center; justify-content: center;
  }
  .label {
    position: relative; width: 920px; height: 980px;
    background: var(--label-white);
    box-shadow: 0 10px 30px rgba(160, 80, 85, 0.18);
    overflow: hidden;
  }
  .label__band {
    position: absolute; left: 0; top: 0; width: 100%; height: 480px;
    background: var(--band-pink);
  }
  .label__pattern {
    position: absolute; inset: 0;
    background: radial-gradient(ellipse at 30% 40%, rgba(255,255,255,0.16), transparent 60%),
                linear-gradient(90deg, var(--band-pink) 0%, var(--band-pink-deep) 100%);
  }
  .brand {
    position: absolute; top: 70px; left: 0; width: 100%;
    display: flex; flex-direction: column; align-items: center;
    font-family: "Montserrat", sans-serif; font-weight: 600;
    color: #fbeff0; text-transform: uppercase; line-height: 1;
  }
  .brand__line1 { font-size: 66px; letter-spacing: 4px; }
  .brand__line2 { font-size: 44px; letter-spacing: 10px; margin-top: 8px; }
  .brand__tagline {
    margin-top: 16px; padding: 6px 26px;
    background: var(--tag-red); border-radius: 4px;
    font-family: "Montserrat", sans-serif; font-weight: 500;
    font-size: 28px; letter-spacing: 1px; text-transform: none;
    color: #fbe9ea;
  }
  .product-name {
    position: absolute; left: 0; width: 100%; text-align: center;
    font-family: "DM Serif Text", serif; line-height: 1;
  }
  .product-name--foaming { top: 330px; font-size: 150px; color: #fff7f6; }
  .product-name--soap { top: 500px; font-size: 116px; color: var(--soap-blue); }
  .claims {
    position: absolute; top: 760px; left: 60px; right: 60px;
    display: flex; justify-content: space-between; align-items: flex-start;
  }
  .claim {
    display: flex; flex-direction: column; align-items: center; width: 170px;
    font-family: "Montserrat", sans-serif; font-weight: 700;
    font-size: 17px; color: var(--icon-blue);
  }
  .claim svg { width: 72px; height: 72px; margin-bottom: 12px; }
  .claims__divider {
    width: 2px; height: 70px; background: var(--icon-blue); opacity: 0.6; margin-top: 8px;
  }
  .net-weight {
    position: absolute; top: 880px; width: 100%; text-align: center;
    font-family: "Montserrat", sans-serif; font-weight: 500;
    font-size: 38px; color: var(--ink-dark);
  }
  .label__stripe {
    position: absolute; left: 0; bottom: 20px; width: 100%; height: 22px;
    background: var(--stripe-pink);
  }
</style>
</head>
<body>
<main class="canvas">
  <section class="label">
    <div class="label__band">
      <div class="label__pattern" role="img" aria-label="Faint pink floral line pattern"></div>
    </div>

    <header class="brand">
      <span class="brand__line1">Plumwick</span>
      <span class="brand__line2">Home</span>
      <span class="brand__tagline">The Plumwick Promise</span>
    </header>

    <h1 class="product-name product-name--foaming">Foaming</h1>
    <h2 class="product-name product-name--soap">Hand Soap</h2>

    <div class="claims">
      <div class="claim">
        <svg viewBox="0 0 72 72"><circle cx="36" cy="36" r="32" fill="none" stroke="currentColor" stroke-width="3"/><path d="M22 37l10 10 19-21" fill="none" stroke="currentColor" stroke-width="4" stroke-linecap="round" stroke-linejoin="round"/></svg>
        All Natural
      </div>
      <span class="claims__divider"></span>
      <div class="claim">
        <svg viewBox="0 0 72 72"><circle cx="36" cy="36" r="32" fill="none" stroke="currentColor" stroke-width="3"/><path d="M22 37l10 10 19-21" fill="none" stroke="currentColor" stroke-width="4" stroke-linecap="round" stroke-linejoin="round"/></svg>
        Paraben Free
      </div>
      <span class="claims__divider"></span>
      <div class="claim">
        <svg viewBox="0 0 72 72"><circle cx="36" cy="36" r="32" fill="none" stroke="currentColor" stroke-width="3"/><path d="M22 37l10 10 19-21" fill="none" stroke="currentColor" stroke-width="4" stroke-linecap="round" stroke-linejoin="round"/></svg>
        100% Vegan
      </div>
      <span class="claims__divider"></span>
      <div class="claim">
        <svg viewBox="0 0 72 72"><circle cx="36" cy="36" r="32" fill="none" stroke="currentColor" stroke-width="3"/><path d="M22 37l10 10 19-21" fill="none" stroke="currentColor" stroke-width="4" stroke-linecap="round" stroke-linejoin="round"/></svg>
        Cruelty Free
      </div>
    </div>

    <p class="net-weight">12 oz</p>
    <div class="label__stripe"></div>
  </section>
</main>
</body>
</html>
```